Kelvo Media ~ Business Card Design Project

Kelvo Media is a digital marketing agency which creates and maintains online social presence for brands and businesses. Services include monthly stream management, social media advertising campaigns, online press release distribution, search engine optimization, copywriting, digital strategy consultation, video marketing campaigns, fan acquisition, and Wordpress website development.
The company is currently rebranding to a full service agency from just a social media firm, with a new website launching soon. I'm looking for an extremely creative and modern business card design that pops out from the rest and fits with our company's sector/services.
It will need to be 1039 x 697 pixels, and rectangular (not rounded edges or corners). Utilize our company logo (file is attached), and include the following information in any design or layout:
Dana Whitlock
CEO/Creative Director
Kelvo Media
Facebook: social.example/kelvomedia
Twitter: @KelvoMedia
Phone: +1 555 014 7281
Cell: +1 555 018 4932
Email: dana@kelvomedia.example
Website: www.kelvomedia.example
418 Brennick Street, Suite 302
Marlow Bay, ON
K0X 4P7

```html
<!DOCTYPE html>
<html lang="en">
<head>
<meta charset="utf-8">
<title>Kelvo Media – Business Card</title>
<link rel="stylesheet" href="https://fonts.googleapis.com/css2?family=Arimo:wght@400;700&display=swap">
<style>
  :root {
    --stage: #d9dee3;
    --brand-blue: #0d3c9e;
    --brand-blue-light: #1d55c0;
    --rule-blue: #2a4f9f;
    --ink: #1e1e1e;
    --ink-soft: #555a60;
    --paper: #ffffff;
    --band-grey: #e7eaef;
    --divider: #2a4f9f;
  }
  * { box-sizing: border-box; margin: 0; padding: 0; }
  html, body {
    width: 1200px; height: 960px; overflow: hidden;
    background: var(--stage);
    font-family: "Arimo", Arial, sans-serif;
  }
  .stage {
    width: 1200px; height: 960px;
    display: flex; flex-direction: column; align-items: center; justify-content: center;
    gap: 56px;
  }
  .card {
    width: 588px; height: 394px;
    position: relative;
    box-shadow: 0 6px 18px rgba(0,0,0,.18);
  }

  /* Front */
  .card--front { background: var(--paper); color: var(--ink); }
  .card__rule {
    position: absolute; left: 34px; right: 16px; top: 74px;
    height: 2px; background: var(--rule-blue);
  }
  .card__name {
    position: absolute; left: 34px; top: 48px;
    font-size: 26px; font-weight: 700; word-spacing: 6px; line-height: 1;
  }
  .card__title {
    position: absolute; left: 34px; top: 84px;
    font-size: 18px; color: var(--ink-soft);
  }
  .wordmark {
    display: flex; align-items: center; gap: 12px;
    font-weight: 400;
  }
  .wordmark__dot { border-radius: 50%; flex: none; }
  .card--front .wordmark {
    position: absolute; left: 0; right: 0; top: 150px; justify-content: center;
    font-size: 32px; color: var(--brand-blue);
  }
  .card--front .wordmark__dot { width: 58px; height: 58px; background: var(--brand-blue); }
  .card__address {
    position: absolute; right: 22px; top: 262px;
    font-size: 15px; color: var(--ink);
  }
  .contact-band {
    position: absolute; left: 0; right: 0; bottom: 40px; height: 54px;
    background: var(--band-grey);
    display: flex; align-items: center; justify-content: flex-end;
    padding: 0 22px; gap: 14px;
    font-size: 15px; color: var(--ink);
  }
  .contact-band__item { display: flex; align-items: center; gap: 8px; white-space: nowrap; }
  .contact-band__divider { width: 2px; height: 26px; background: var(--divider); }
  .icon { width: 14px; height: 14px; flex: none; }

  /* Back */
  .card--back { background: var(--brand-blue); color: var(--paper); }
  .card--back .wordmark {
    position: absolute; left: 0; right: 0; top: 118px; justify-content: center;
    font-size: 42px; color: var(--paper);
  }
  .card--back .wordmark__dot { width: 82px; height: 82px; background: var(--paper); }
  .social-band {
    position: absolute; left: 0; right: 0; bottom: 40px; height: 36px;
    background: var(--brand-blue-light);
    display: flex; align-items: center; justify-content: space-between;
    padding: 0 22px;
    font-size: 14px; letter-spacing: .3px;
  }
  .social-band__item { display: flex; align-items: center; gap: 7px; white-space: nowrap; }
  .social-band__mark {
    width: 12px; height: 12px; border-radius: 50%;
    background: rgba(255,255,255,.85);
  }
</style>
</head>
<body>
<main class="stage">

  <section class="card card--front" aria-label="Business card front">
    <div class="card__rule"></div>
    <h1 class="card__name">Dana Whitlock</h1>
    <p class="card__title">CEO/Creative Director</p>
    <div class="wordmark"><span class="wordmark__dot"></span><span>KelvoMedia</span></div>
    <p class="card__address">418 Brennick Street, Suite 302, Marlow Bay, ON, K0X 4P7</p>
    <div class="contact-band">
      <span class="contact-band__item">
        <svg class="icon" viewBox="0 0 14 14" aria-hidden="true"><rect x="3.5" y="1" width="7" height="12" rx="1.2" fill="none" stroke="#2a4f9f" stroke-width="1.4"/><rect x="5" y="3" width="4" height="4" fill="#2a4f9f"/></svg>
        +1 555 014 7281
      </span>
      <span class="contact-band__divider"></span>
      <span class="contact-band__item">
        <svg class="icon" viewBox="0 0 14 14" aria-hidden="true"><rect x="2" y="1" width="10" height="12" rx="1" fill="none" stroke="#2a4f9f" stroke-width="1.4"/><line x1="5" y1="4" x2="10" y2="4" stroke="#2a4f9f" stroke-width="1.2"/><line x1="5" y1="7" x2="10" y2="7" stroke="#2a4f9f" stroke-width="1.2"/><line x1="5" y1="10" x2="10" y2="10" stroke="#2a4f9f" stroke-width="1.2"/></svg>
        +1 555 018 4932
      </span>
      <span class="contact-band__divider"></span>
      <span class="contact-band__item">
        <svg class="icon" viewBox="0 0 14 14" aria-hidden="true"><rect x="1" y="3" width="12" height="8.5" fill="none" stroke="#2a4f9f" stroke-width="1.4"/><polyline points="1,3 7,8 13,3" fill="none" stroke="#2a4f9f" stroke-width="1.4"/></svg>
        dana@kelvomedia.example
      </span>
    </div>
  </section>

  <section class="card card--back" aria-label="Business card back">
    <div class="wordmark"><span class="wordmark__dot"></span><span>KelvoMedia</span></div>
    <div class="social-band">
      <span class="social-band__item"><span class="social-band__mark"></span>social.example/kelvomedia</span>
      <span class="social-band__item"><span class="social-band__mark"></span>@KelvoMedia</span>
      <span class="social-band__item">
        <svg class="icon" viewBox="0 0 14 14" aria-hidden="true"><circle cx="7" cy="7" r="5.5" fill="none" stroke="#fff" stroke-width="1.3"/><ellipse cx="7" cy="7" rx="2.4" ry="5.5" fill="none" stroke="#fff" stroke-width="1.1"/><line x1="1.5" y1="7" x2="12.5" y2="7" stroke="#fff" stroke-width="1.1"/></svg>
        www.kelvomedia.example
      </span>
    </div>
  </section>

</main>
</body>
</html>
```